Sales presentation introduction for Finance and Tech firms

Our business is two fold - 1) recruitment 2) consultancy. We would like a one or two page template that we can use to send to potential clients. The template will ideally be the same for the recruitment and consultancy side. We need to be able to edit the template to enter text.

I have attached our logo so you can see what we currently use on Trovella.

Sector is financial services and technology. We do not intent to have lots of text but the layout/images/designs to be used should cover some of page in a way that it takes up some space to avoid having to write lot of text.

Open to colour suggestions.

Please look at the attached word doc to see the text I would like for the two presentations.

Happy to answer questions.

Target Market(s)

Directors

Industry/Entity Type

Finance and tech companies

Colors
0094D4
00A9DD
6FCCEA
C7EBF8
E9F6FB

Requirements
Must have
• Editable text

```html
<!DOCTYPE html>
<html lang="en">
<head>
<meta charset="utf-8">
<title>Meridian K7 – Consultancy and Recruitment Flyers</title>
<link rel="stylesheet" href="https://fonts.googleapis.com/css2?family=Barlow:wght@500;600;700&family=Roboto:wght@400;500;700&display=swap">
<style>
:root{
  --board:#7a7a7a;
  --paper:#ffffff;
  --band:#1b7ec3;
  --blue-deep:#0c57a5;
  --blue-mid:#1c82c6;
  --sky:#6fcaea;
  --pale:#e4f4fc;
  --ink:#231f20;
  --ink-soft:#3b3839;
  --footer:#2a2627;
  --heading-font:"Barlow",sans-serif;
  --body-font:"Roboto",sans-serif;
}
*{box-sizing:border-box;margin:0;padding:0}
html,body{width:958px;height:1200px;overflow:hidden}
body{background:var(--board);position:relative;font-family:var(--body-font);color:var(--ink)}
.page{position:absolute;width:377px;height:533px;background:var(--paper);overflow:hidden}
.page--tl{left:82px;top:58px}
.page--tr{left:493px;top:58px}
.page--bl{left:82px;top:623px}
.page--br{left:493px;top:623px}
.masthead{position:absolute;left:0;top:0;width:377px;height:137px}
.brand{position:absolute;left:22px;top:58px;font-family:var(--heading-font);font-weight:500;font-size:17px;letter-spacing:1.3px;color:var(--ink)}
.tagline{position:absolute;left:23px;top:94px;width:270px;font-family:var(--heading-font);font-weight:600;font-size:9.1px;line-height:11.6px;color:#fff;white-space:nowrap}
.section-title{position:absolute;left:23px;top:143px;font-family:var(--heading-font);font-weight:700;font-size:10.8px;color:var(--ink);letter-spacing:.1px}
.intro{position:absolute;left:23px;width:332px;font-size:6.4px;line-height:8.8px;text-align:justify;color:var(--ink)}
.intro p+p{margin-top:2px}
.intro .accent{color:var(--blue-mid);font-weight:500}
.service-grid{position:absolute;left:23px;list-style:none;display:grid;grid-template-columns:122px 126px 100px;row-gap:8px}
.page--consult .service-grid{top:236px;row-gap:8.5px}
.page--recruit .service-grid{top:373px;row-gap:12px}
.service{display:flex;align-items:center;height:33px}
.service svg{width:33px;height:33px;flex:none}
.service span{margin-left:10px;font-size:7.2px;line-height:9.2px;color:var(--ink-soft)}
.features{position:absolute;left:0;top:362px;width:377px;height:146px;background:var(--pale)}
.feature{position:absolute;display:flex}
.feature svg{width:34px;height:34px;flex:none;margin-right:6px}
.feature h3{font-family:var(--heading-font);font-weight:600;font-size:8.2px;color:var(--blue-mid);line-height:9px;margin-bottom:1.5px}
.feature p{font-size:4.9px;line-height:6.8px;text-align:justify;color:var(--ink-soft)}
.feature--a{left:22px;top:6px}
.feature--b{left:197px;top:6px}
.feature--c{left:22px;top:87px}
.feature--d{left:197px;top:87px}
.feature div{width:117px}
.contact-bar{position:absolute;left:0;bottom:0;width:377px;height:25px;background:var(--footer);display:flex;align-items:center;justify-content:space-between;padding:0 22px;color:#fff;font-family:var(--heading-font);font-weight:500;font-size:8px}
.contact-bar span{display:flex;align-items:center}
.contact-bar svg{width:12px;height:12px;margin-right:4px}
.recruit-cols{position:absolute;left:23px;top:234px;width:332px;font-size:5.4px;line-height:7.2px;color:var(--ink);font-weight:500}
.recruit-cols .col-left{position:absolute;left:0;top:0;width:155px;text-align:justify}
.recruit-cols .col-right{position:absolute;left:174px;top:0;width:158px;text-align:justify}
.ticks{list-style:none;margin-top:6px;text-align:left}
.ticks li{position:relative;padding-left:7px;margin-bottom:4.3px;font-size:5.6px}
.ticks li::before{content:"";position:absolute;left:0;top:2px;width:3.6px;height:3.6px;border-radius:50%;background:var(--blue-mid)}
.tick-grid{list-style:none;display:grid;grid-template-columns:80px 69px;column-gap:9px;row-gap:7px;margin-top:6px;text-align:left}
.tick-grid li{position:relative;padding-left:7px;font-size:5.1px;line-height:6.6px;height:28px;min-width:0;overflow-wrap:break-word}
.tick-grid li::before{content:"";position:absolute;left:0;top:1.5px;width:3.6px;height:3.6px;border-radius:50%;background:var(--blue-mid)}
.recruit-note{position:absolute;left:23px;top:346px;width:332px;font-size:5.4px;line-height:7.3px;font-weight:500;color:var(--ink)}
</style>
</head>
<body>

<svg width="0" height="0" style="position:absolute" aria-hidden="true">
  <defs>
    <linearGradient id="sky-towers" x1="0" y1="0" x2="1" y2="1">
      <stop offset="0" stop-color="#d9ecf8"/>
      <stop offset=".5" stop-color="#8fb9de"/>
      <stop offset="1" stop-color="#3d6fa6"/>
    </linearGradient>
    <radialGradient id="tech-glow" cx=".72" cy=".45" r=".7">
      <stop offset="0" stop-color="#5fc4ef"/>
      <stop offset=".3" stop-color="#1b5a8f"/>
      <stop offset="1" stop-color="#0a1d3a"/>
    </radialGradient>
    <symbol id="svc-doc" viewBox="0 0 33 33">
      <circle cx="16.5" cy="16.5" r="16.5" fill="#1c82c6"/>
      <circle cx="16.5" cy="16.5" r="14" fill="none" stroke="#fff" stroke-width=".9"/>
      <rect x="11" y="9" width="11" height="14" rx="1" fill="none" stroke="#fff" stroke-width="1"/>
      <path d="M13 13h7M13 16h7M13 19h5" stroke="#fff" stroke-width=".9"/>
    </symbol>
    <symbol id="svc-chart" viewBox="0 0 33 33">
      <circle cx="16.5" cy="16.5" r="16.5" fill="#1c82c6"/>
      <circle cx="16.5" cy="16.5" r="14" fill="none" stroke="#fff" stroke-width=".9"/>
      <path d="M10 23h13M11.5 22v-4M15 22v-6M18.5 22v-8M22 22v-10" stroke="#fff" stroke-width="1.4"/>
    </symbol>
    <symbol id="svc-search" viewBox="0 0 33 33">
      <circle cx="16.5" cy="16.5" r="16.5" fill="#1c82c6"/>
      <circle cx="16.5" cy="16.5" r="14" fill="none" stroke="#fff" stroke-width=".9"/>
      <circle cx="15" cy="15" r="5" fill="none" stroke="#fff" stroke-width="1.1"/>
      <path d="M18.6 18.6l4 4" stroke="#fff" stroke-width="1.4"/>
    </symbol>
    <symbol id="ft-gear" viewBox="0 0 34 34">
      <circle cx="17" cy="18" r="10" fill="none" stroke="#0c57a5" stroke-width="1.4" stroke-dasharray="3 1.6"/>
      <rect x="12" y="14" width="10" height="8" rx="1" fill="none" stroke="#0c57a5" stroke-width="1.2"/>
      <path d="M5 7v5M8 5v7M11 8v4" stroke="#0c57a5" stroke-width="1.2"/>
    </symbol>
    <symbol id="ft-bulb" viewBox="0 0 34 34">
      <circle cx="12" cy="11" r="7" fill="none" stroke="#0c57a5" stroke-width="1.3"/>
      <path d="M9 20h6M10 23h4" stroke="#0c57a5" stroke-width="1.2"/>
      <circle cx="25" cy="25" r="5" fill="none" stroke="#0c57a5" stroke-width="1.3"/>
      <path d="M18 8h6v6" fill="none" stroke="#0c57a5" stroke-width="1"/>
    </symbol>
    <symbol id="ft-laptop" viewBox="0 0 34 34">
      <rect x="5" y="10" width="20" height="14" rx="1" fill="none" stroke="#0c57a5" stroke-width="1.3"/>
      <path d="M2 27h26" stroke="#0c57a5" stroke-width="1.4"/>
      <circle cx="22" cy="10" r="6" fill="#fff" stroke="#0c57a5" stroke-width="1.3"/>
    </symbol>
    <symbol id="ft-org" viewBox="0 0 34 34">
      <circle cx="17" cy="8" r="5" fill="none" stroke="#0c57a5" stroke-width="1.3"/>
      <path d="M17 13v6M6 19h22M6 19v4M17 19v4M28 19v4" stroke="#0c57a5" stroke-width="1.2"/>
      <rect x="3" y="23" width="6" height="5" fill="none" stroke="#0c57a5" stroke-width="1.2"/>
      <rect x="14" y="23" width="6" height="5" fill="none" stroke="#0c57a5" stroke-width="1.2"/>
      <rect x="25" y="23" width="6" height="5" fill="none" stroke="#0c57a5" stroke-width="1.2"/>
    </symbol>
    <symbol id="ic-phone" viewBox="0 0 12 12">
      <circle cx="6" cy="6" r="5.4" fill="none" stroke="#fff" stroke-width=".8"/>
      <path d="M4 3.5l1 .3.3 1.2-.6.5a4 4 0 0 0 1.8 1.8l.5-.6 1.2.3.3 1-.6.6C5.6 8.4 3.6 6.4 3.4 4.1z" fill="#fff"/>
    </symbol>
    <symbol id="ic-mail" viewBox="0 0 12 12">
      <circle cx="6" cy="6" r="5.4" fill="none" stroke="#fff" stroke-width=".8"/>
      <rect x="3.3" y="4.2" width="5.4" height="3.8" fill="none" stroke="#fff" stroke-width=".7"/>
      <path d="M3.3 4.2L6 6.4l2.7-2.2" fill="none" stroke="#fff" stroke-width=".7"/>
    </symbol>
    <symbol id="ic-web" viewBox="0 0 12 12">
      <circle cx="6" cy="6" r="5.4" fill="none" stroke="#fff" stroke-width=".8"/>
      <circle cx="6" cy="6" r="3" fill="none" stroke="#fff" stroke-width=".7"/>
      <path d="M3 6h6M6 3c-1.4 1.8-1.4 4.2 0 6M6 3c1.4 1.8 1.4 4.2 0 6" fill="none" stroke="#fff" stroke-width=".6"/>
    </symbol>
  </defs>
</svg>

<!-- ============ Consultancy, city photo ============ -->
<section class="page page--consult page--tl">
  <svg class="masthead" viewBox="0 0 377 137">
    <polygon points="0,87 276,87 326,137 0,137" fill="var(--band)"/>
    <g role="img" aria-label="Photo of glass office towers against a bright sky">
      <polygon points="185,0 377,0 377,84 328,130" fill="url(#sky-towers)"/>
    </g>
    <polygon points="326,137 377,88 377,95 334,137" fill="var(--blue-deep)"/>
    <polygon points="346,137 377,106 377,137" fill="var(--sky)"/>
  </svg>
  <div class="brand">MERIDIAN K7</div>
  <p class="tagline">A partner who brings new and innovative ideas to the table,<br>through extensive industry experience and knowledge.<br>Meridian will ensure you are prepared for growth.</p>
  <h2 class="section-title">MERIDIAN CONSULTANCY</h2>
  <div class="intro" style="top:158px">
    <p>Meridian K7 is a bespoke consultancy firm that specialises in buy side investment. Through an industry based consultative approach we assist our clients in preparing for, and facilitating, long term growth. Working closely with our clients we combine innovative thinking and breakthrough technologies to accelerate progress and, together, achieve enduring results.</p>
    <p>Experienced in successfully delivering change for global organisations as well as assisting smaller firms during their growth phase. Meridian will work with you create a workable model and ensure successful delivery of the project.</p>
  </div>
  <ul class="service-grid">
    <li class="service"><svg><use href="#svc-doc"/></svg><span>Order<br>Management<br>and Trading</span></li>
    <li class="service"><svg><use href="#svc-search"/></svg><span>CRM/ Onboarding</span></li>
    <li class="service"><svg><use href="#svc-doc"/></svg><span>Compliance</span></li>
    <li class="service"><svg><use href="#svc-chart"/></svg><span>Investment<br>and<br>Research</span></li>
    <li class="service"><svg><use href="#svc-search"/></svg><span>Performance,<br>Risk and<br>Attribution</span></li>
    <li class="service"><svg><use href="#svc-chart"/></svg><span>Finance<br>and<br>Accounting</span></li>
    <li class="service"><svg><use href="#svc-search"/></svg><span>Investment<br>and<br>Research</span></li>
    <li class="service"><svg><use href="#svc-doc"/></svg><span>Client and<br>Regulatory<br>Reporting</span></li>
    <li class="service"><svg><use href="#svc-chart"/></svg><span>Middle<br>and<br>Back Office</span></li>
  </ul>
  <div class="features">
    <div class="feature feature--a"><svg><use href="#ft-gear"/></svg><div><h3>Business Strategy</h3><p>Meridian will help you create a business strategy tailored to your requirements. Ensuing each business process is defined and taken into account allows for a successful design. Creating and implementing an operating model that takes into account budget, resources, culture and your company's vision.</p></div></div>
    <div class="feature feature--b"><svg><use href="#ft-bulb"/></svg><div><h3>Change management</h3><p>Meridian works with clients to deliver bespoke change initiatives. Rigorous business analysis and risk management allows for successful change initiatives. We work with you throughout the complete process, to ensure that delivery is based on value. Transition phases are challenging aspects of change initiatives which is why our team manage all transitions and the risk they carry.</p></div></div>
    <div class="feature feature--c"><svg><use href="#ft-laptop"/></svg><div><h3>IT transformation</h3><p>Meridian is widely experienced in a range of technologies. We help with the implementation of software provider or design and develop bespoke services. Covering front to back office the team specialises in full project lifecycle from feasibility through to implementation.</p></div></div>
    <div class="feature feature--d"><svg><use href="#ft-org"/></svg><div><h3>Organisational structure</h3><p>Meridian works with clients to improve resource capability and strategic partnerships. Acting as an extension of the HR function, we analyse business processes and ensure that our clients have the ability to manage changing workforce demands.</p></div></div>
  </div>
  <footer class="contact-bar">
    <span><svg><use href="#ic-phone"/></svg>+44 (0) 7700 900123</span>
    <span><svg><use href="#ic-mail"/></svg>info@meridiank7.com</span>
    <span><svg><use href="#ic-web"/></svg>www.meridiank7.com</span>
  </footer>
</section>

<!-- ============ Consultancy, technology visual ============ -->
<section class="page page--consult page--tr">
  <svg class="masthead" viewBox="0 0 377 137">
    <polygon points="0,87 276,87 326,137 0,137" fill="var(--band)"/>
    <g role="img" aria-label="Dark blue digital network visual with glowing connected nodes">
      <polygon points="185,0 377,0 377,84 328,130" fill="url(#tech-glow)"/>
    </g>
    <polygon points="326,137 377,88 377,95 334,137" fill="var(--blue-deep)"/>
    <polygon points="346,137 377,106 377,137" fill="var(--sky)"/>
  </svg>
  <div class="brand">MERIDIAN K7</div>
  <p class="tagline">A partner who brings new and innovative ideas to the table,<br>through extensive industry experience and knowledge.<br>Meridian will ensure you are prepared for growth.</p>
  <h2 class="section-title">MERIDIAN CONSULTANCY</h2>
  <div class="intro" style="top:158px">
    <p>Meridian K7 is a bespoke consultancy firm that specialises in buy side investment. Through an industry based consultative approach we assist our clients in preparing for, and facilitating, long term growth. Working closely with our clients we combine innovative thinking and breakthrough technologies to accelerate progress and, together, achieve enduring results.</p>
    <p>Experienced in successfully delivering change for global organisations as well as assisting smaller firms during their growth phase. Meridian will work with you create a workable model and ensure successful delivery of the project.</p>
  </div>
  <ul class="service-grid">
    <li class="service"><svg><use href="#svc-doc"/></svg><span>Order<br>Management<br>and Trading</span></li>
    <li class="service"><svg><use href="#svc-search"/></svg><span>CRM/ Onboarding</span></li>
    <li class="service"><svg><use href="#svc-doc"/></svg><span>Compliance</span></li>
    <li class="service"><svg><use href="#svc-chart"/></svg><span>Investment<br>and<br>Research</span></li>
    <li class="service"><svg><use href="#svc-search"/></svg><span>Performance,<br>Risk and<br>Attribution</span></li>
    <li class="service"><svg><use href="#svc-chart"/></svg><span>Finance<br>and<br>Accounting</span></li>
    <li class="service"><svg><use href="#svc-search"/></svg><span>Investment<br>and<br>Research</span></li>
    <li class="service"><svg><use href="#svc-doc"/></svg><span>Client and<br>Regulatory<br>Reporting</span></li>
    <li class="service"><svg><use href="#svc-chart"/></svg><span>Middle<br>and<br>Back Office</span></li>
  </ul>
  <div class="features">
    <div class="feature feature--a"><svg><use href="#ft-gear"/></svg><div><h3>Business Strategy</h3><p>Meridian will help you create a business strategy tailored to your requirements. Ensuing each business process is defined and taken into account allows for a successful design. Creating and implementing an operating model that takes into account budget, resources, culture and your company's vision.</p></div></div>
    <div class="feature feature--b"><svg><use href="#ft-bulb"/></svg><div><h3>Change management</h3><p>Meridian works with clients to deliver bespoke change initiatives. Rigorous business analysis and risk management allows for successful change initiatives. We work with you throughout the complete process, to ensure that delivery is based on value. Transition phases are challenging aspects of change initiatives which is why our team manage all transitions and the risk they carry.</p></div></div>
    <div class="feature feature--c"><svg><use href="#ft-laptop"/></svg><div><h3>IT transformation</h3><p>Meridian is widely experienced in a range of technologies. We help with the implementation of software provider or design and develop bespoke services. Covering front to back office the team specialises in full project lifecycle from feasibility through to implementation.</p></div></div>
    <div class="feature feature--d"><svg><use href="#ft-org"/></svg><div><h3>Organisational structure</h3><p>Meridian works with clients to improve resource capability and strategic partnerships. Acting as an extension of the HR function, we analyse business processes and ensure that our clients have the ability to manage changing workforce demands.</p></div></div>
  </div>
  <footer class="contact-bar">
    <span><svg><use href="#ic-phone"/></svg>+44 (0) 7700 900123</span>
    <span><svg><use href="#ic-mail"/></svg>info@meridiank7.com</span>
    <span><svg><use href="#ic-web"/></svg>www.meridiank7.com</span>
  </footer>
</section>

<!-- ============ Recruitment, city photo ============ -->
<section class="page page--recruit page--bl">
  <svg class="masthead" viewBox="0 0 377 137">
    <polygon points="0,87 276,87 326,137 0,137" fill="var(--band)"/>
    <g role="img" aria-label="Photo of glass office towers against a bright sky">
      <polygon points="185,0 377,0 377,84 328,130" fill="url(#sky-towers)"/>
    </g>
    <polygon points="326,137 377,88 377,95 334,137" fill="var(--blue-deep)"/>
    <polygon points="346,137 377,106 377,137" fill="var(--sky)"/>
  </svg>
  <div class="brand">MERIDIAN K7</div>
  <p class="tagline">A partner who brings new and innovative ideas to the table,<br>through extensive industry experience and knowledge.<br>Meridian will ensure you are prepared for growth.</p>
  <h2 class="section-title">MERIDIAN RECRUITMENT</h2>
  <div class="intro" style="top:159px;font-size:6.9px;line-height:8.7px">
    <p>Meridian is more than an ordinary recruitment service. Our experts work with clients to develop a HR strategy that maps current, and impending, organisational needs; using research to effectively benchmark. We are developing various talent communities that provide effective, and timely, recruitment solutions for our clients.</p>
    <p><span class="accent">Specialists in:</span> Asset Management recruitment with a specialisation in I.T, Operations, Regulation and Change Management.</p>
  </div>
  <div class="recruit-cols">
    <div class="col-left">
      <p>Meridian acts as an extension of your HR function, providing an end-to-end permanent and contingent talent acquisition solution, taking full accountability and ownership for the entire recruitment process, which includes:</p>
      <ul class="ticks">
        <li>Workforce Planning</li>
        <li>Strategic Sourcing</li>
        <li>Talent Engagement</li>
        <li>Candidate Management</li>
        <li>Weekly vacancy updates</li>
      </ul>
    </div>
    <div class="col-right">
      <p>We recognise that hiring can be a lengthy process, therefore we partner with you to ensure you only interview top quantile candidates, cutting out multiple meetings with multiple candidates. Giving hiring managers time back in their diaries to do their day jobs and reducing the time to hire. This is achieved by:</p>
      <ul class="tick-grid">
        <li>Understanding the roles, and partnering with you to build meaningful job descriptions</li>
        <li>Support with interviews and we ensure the candidate has a positive experience</li>
        <li>Candidates are fully screened and interviewed prior to presentation to you</li>
        <li>Qualified shortlist of top 3 candidates</li>
      </ul>
    </div>
  </div>
  <p class="recruit-note">Meridian recruitment partners with principal business consultants from Meridian consultancy to ensure candidates are properly screened before presenting to our clients. This allows for our clients to focus on only interviewing the best on the market.</p>
  <ul class="service-grid">
    <li class="service"><svg><use href="#svc-doc"/></svg><span>Order<br>Management<br>and Trading</span></li>
    <li class="service"><svg><use href="#svc-search"/></svg><span>CRM/ Onboarding</span></li>
    <li class="service"><svg><use href="#svc-doc"/></svg><span>Compliance</span></li>
    <li class="service"><svg><use href="#svc-chart"/></svg><span>Investment<br>and<br>Research</span></li>
    <li class="service"><svg><use href="#svc-search"/></svg><span>Performance,<br>Risk and<br>Attribution</span></li>
    <li class="service"><svg><use href="#svc-chart"/></svg><span>Finance<br>and<br>Accounting</span></li>
    <li class="service"><svg><use href="#svc-search"/></svg><span>Investment<br>and<br>Research</span></li>
    <li class="service"><svg><use href="#svc-doc"/></svg><span>Client and<br>Regulatory<br>Reporting</span></li>
    <li class="service"><svg><use href="#svc-chart"/></svg><span>Middle<br>and<br>Back Office</span></li>
  </ul>
  <footer class="contact-bar">
    <span><svg><use href="#ic-phone"/></svg>+44 (0) 7700 900123</span>
    <span><svg><use href="#ic-mail"/></svg>info@meridiank7.com</span>
    <span><svg><use href="#ic-web"/></svg>www.meridiank7.com</span>
  </footer>
</section>

<!-- ============ Recruitment, technology visual ============ -->
<section class="page page--recruit page--br">
  <svg class="masthead" viewBox="0 0 377 137">
    <polygon points="0,87 276,87 326,137 0,137" fill="var(--band)"/>
    <g role="img" aria-label="Dark blue digital network visual with glowing connected nodes">
      <polygon points="185,0 377,0 377,84 328,130" fill="url(#tech-glow)"/>
    </g>
    <polygon points="326,137 377,88 377,95 334,137" fill="var(--blue-deep)"/>
    <polygon points="346,137 377,106 377,137" fill="var(--sky)"/>
  </svg>
  <div class="brand">MERIDIAN K7</div>
  <p class="tagline">A partner who brings new and innovative ideas to the table,<br>through extensive industry experience and knowledge.<br>Meridian will ensure you are prepared for growth.</p>
  <h2 class="section-title">MERIDIAN RECRUITMENT</h2>
  <div class="intro" style="top:159px;font-size:6.9px;line-height:8.7px">
    <p>Meridian is more than an ordinary recruitment service. Our experts work with clients to develop a HR strategy that maps current, and impending, organisational needs; using research to effectively benchmark. We are developing various talent communities that provide effective, and timely, recruitment solutions for our clients.</p>
    <p><span class="accent">Specialists in:</span> Asset Management recruitment with a specialisation in I.T, Operations, Regulation and Change Management.</p>
  </div>
  <div class="recruit-cols">
    <div class="col-left">
      <p>Meridian acts as an extension of your HR function, providing an end-to-end permanent and contingent talent acquisition solution, taking full accountability and ownership for the entire recruitment process, which includes:</p>
      <ul class="ticks">
        <li>Workforce Planning</li>
        <li>Strategic Sourcing</li>
        <li>Talent Engagement</li>
        <li>Candidate Management</li>
        <li>Weekly vacancy updates</li>
      </ul>
    </div>
    <div class="col-right">
      <p>We recognise that hiring can be a lengthy process, therefore we partner with you to ensure you only interview top quantile candidates, cutting out multiple meetings with multiple candidates. Giving hiring managers time back in their diaries to do their day jobs and reducing the time to hire. This is achieved by:</p>
      <ul class="tick-grid">
        <li>Understanding the roles, and partnering with you to build meaningful job descriptions</li>
        <li>Support with interviews and we ensure the candidate has a positive experience</li>
        <li>Candidates are fully screened and interviewed prior to presentation to you</li>
        <li>Qualified shortlist of top 3 candidates</li>
      </ul>
    </div>
  </div>
  <p class="recruit-note">Meridian recruitment partners with principal business consultants from Meridian consultancy to ensure candidates are properly screened before presenting to our clients. This allows for our clients to focus on only interviewing the best on the market.</p>
  <ul class="service-grid">
    <li class="service"><svg><use href="#svc-doc"/></svg><span>Order<br>Management<br>and Trading</span></li>
    <li class="service"><svg><use href="#svc-search"/></svg><span>CRM/ Onboarding</span></li>
    <li class="service"><svg><use href="#svc-doc"/></svg><span>Compliance</span></li>
    <li class="service"><svg><use href="#svc-chart"/></svg><span>Investment<br>and<br>Research</span></li>
    <li class="service"><svg><use href="#svc-search"/></svg><span>Performance,<br>Risk and<br>Attribution</span></li>
    <li class="service"><svg><use href="#svc-chart"/></svg><span>Finance<br>and<br>Accounting</span></li>
    <li class="service"><svg><use href="#svc-search"/></svg><span>Investment<br>and<br>Research</span></li>
    <li class="service"><svg><use href="#svc-doc"/></svg><span>Client and<br>Regulatory<br>Reporting</span></li>
    <li class="service"><svg><use href="#svc-chart"/></svg><span>Middle<br>and<br>Back Office</span></li>
  </ul>
  <footer class="contact-bar">
    <span><svg><use href="#ic-phone"/></svg>+44 (0) 7700 900123</span>
    <span><svg><use href="#ic-mail"/></svg>info@meridiank7.com</span>
    <span><svg><use href="#ic-web"/></svg>www.meridiank7.com</span>
  </footer>
</section>

</body>
</html>
```